Disability and mental health support work company requires business card

Specialising
Wrenfield Disability is a new QCAP service aimed toward QCAP participants with a history of criminal justice, psychosocial/mental health, intellectual, and cognitive disabilities.

Our focus
Focusing on providing core QCAP supports for community participation, daily activities and supported independent living.

Authentic
Likeminded people wanting to make a difference in participant's lives.

Our aim to provide holistic and empowering supports targeted towards creating independence and guidance for all participants and families.
Over 35 years of experience working with people that have psychosocial, intellectual, and cognitive disabilities.

Industry/Entity Type

disability and mental health

Contact Information for Business Card

logo - business name

Colors
0054AA
0677BA
7BADD7
CADEEF
E8F1F8
FFF300
FFF600
FEFA6F
FFFEC7
FFFEE8

Requirements
Must have
• want double sided business cards(wont let me change it)
Should not have
• any disability related pictures

```html
<!DOCTYPE html>
<html lang="en">
<head>
<meta charset="utf-8">
<title>Wrenfield Disability – Business Card</title>
<link href="https://fonts.googleapis.com/css2?family=Montserrat:wght@400;500;700&display=swap" rel="stylesheet">
<style>
  :root{
    --navy:#14375e;
    --sky:#7fb0dd;
    --gold:#f0b72a;
    --ink:#2b2f36;
    --paper:#ffffff;
    --backdrop:#8a8987;
  }
  *{box-sizing:border-box;margin:0;padding:0}
  html,body{width:1200px;height:801px;overflow:hidden}
  body{background:var(--backdrop);font-family:'Montserrat',sans-serif;position:relative}
  .card{position:absolute;top:245px;width:540px;height:310px;overflow:hidden;box-shadow:0 6px 18px rgba(0,0,0,.25)}
  .card-front{left:40px;background:var(--paper)}
  .card-back{left:620px;background:var(--navy)}

  /* front */
  .brand-seal{position:absolute;top:22px;right:36px;width:96px;height:96px;border-radius:50%;
    background:var(--navy);border:2px solid var(--sky);display:flex;align-items:center;justify-content:center;
    color:var(--sky);font-weight:700;font-size:11px;letter-spacing:.5px;text-align:center;line-height:1.25}
  .holder{position:absolute;left:36px;top:150px}
  .holder-name{color:var(--navy);font-weight:700;font-size:22px;letter-spacing:.3px}
  .holder-role{color:var(--sky);font-weight:500;font-size:15px;margin-top:2px}
  .divider{position:absolute;left:36px;right:36px;top:206px;height:1px;background:var(--sky)}
  .contacts{position:absolute;left:36px;top:218px;list-style:none;color:var(--ink);font-size:12.5px;line-height:20px}
  .contacts li{display:flex;align-items:center;gap:8px}
  .contacts svg{width:11px;height:11px;flex:none}
  .address{position:absolute;right:36px;top:226px;text-align:right;color:var(--ink);font-size:12.5px;line-height:20px}
  .edge-band{position:absolute;left:0;right:0;bottom:0;height:9px;display:flex}
  .edge-band .navy{flex:54;background:var(--navy)}
  .edge-band .sky{flex:34;background:var(--sky)}
  .edge-band .gold{flex:30;background:var(--gold)}

  /* back */
  .back-name{position:absolute;top:34px;right:36px;color:var(--sky);font-weight:700;font-size:26px;letter-spacing:1.5px;text-align:right;line-height:1.15}
  .burst-area{position:absolute;left:0;right:0;bottom:0;height:190px;
    background:radial-gradient(ellipse 70% 100% at 50% 100%, rgba(240,183,42,.35), rgba(240,183,42,.08) 65%, rgba(240,183,42,0) 100%)}
</style>
</head>
<body>
  <section class="card card-front">
    <div class="brand-seal">WRENFIELD<br>DISABILITY</div>
    <div class="holder">
      <p class="holder-name">OWEN CARLISLE</p>
      <p class="holder-role">President</p>
    </div>
    <div class="divider"></div>
    <ul class="contacts">
      <li><svg viewBox="0 0 12 12"><path d="M3 1l2 2.5-1.2 1.2a7 7 0 0 0 3.5 3.5L8.5 7 11 9l-1.5 2C5 11 1 7 1 2.5z" fill="var(--gold)"/></svg>555-310-4821</li>
      <li><svg viewBox="0 0 12 12"><rect x="1" y="2.5" width="10" height="7" fill="var(--gold)"/><path d="M1 2.5l5 4 5-4" stroke="#fff" fill="none"/></svg>info@wrenfielddisability.com</li>
      <li><svg viewBox="0 0 12 12"><circle cx="6" cy="6" r="5" fill="var(--gold)"/><path d="M1 6h10M6 1c-2 3-2 7 0 10M6 1c2 3 2 7 0 10" stroke="#fff" stroke-width=".8" fill="none"/></svg>www.wrenfielddisability.com</li>
    </ul>
    <p class="address">18 Marlow Quay<br>Harbor Bend CA 90210</p>
    <div class="edge-band"><span class="navy"></span><span class="sky"></span><span class="gold"></span></div>
  </section>

  <section class="card card-back">
    <p class="back-name">WRENFIELD<br>DISABILITY</p>
    <div class="burst-area" role="img" aria-label="Hand-drawn golden sunburst rays rising from the bottom edge"></div>
  </section>
</body>
</html>
```